Business Card Design

I need a Business Card that will catch the attention that will not get thrown in a Drawer. I have 23 companies I use for Auto, Home, Life, and Business Insurance. I make sure that people have the best coverage for the $ spent.

Industry/Entity Type

Business

Contact Information for Business Card

Dorlin Insurance Agency, Inc., Marcus Helgren, 4375 West Tamber Lane Corvale, Ohio 45192 555-281-7496, www.dorlinagency.example, Circlebook, ProLink, Gather+

```html
<!DOCTYPE html>
<html lang="en">
<head>
<meta charset="utf-8">
<title>Dorlin Insurance Agency – Business Card</title>
<link rel="stylesheet" href="https://fonts.googleapis.com/css2?family=Questrial&display=swap">
<style>
  :root {
    --backdrop: #d9d6d2;
    --card: #5b5b5b;
    --accent: #19a6e3;
  }
  html, body {
    margin: 0;
    width: 1200px;
    height: 751px;
    overflow: hidden;
    background: var(--backdrop);
  }
  .business-card {
    position: absolute;
    left: 100px;
    top: 89px;
    width: 1000px;
    height: 572px;
    background: var(--card);
    color: var(--accent);
    font-family: "Questrial", sans-serif;
    text-align: center;
  }
  .agency-name {
    position: absolute;
    top: 78px;
    left: 0;
    right: 0;
    margin: 0;
    font-size: 31px;
    font-weight: 400;
  }
  .divider-swoosh {
    position: absolute;
    left: 90px;
    top: 138px;
    width: 820px;
    height: 40px;
  }
  .agent-name {
    position: absolute;
    top: 196px;
    left: 0;
    right: 0;
    margin: 0;
    font-size: 31px;
    font-weight: 400;
  }
  .contact-details {
    position: absolute;
    top: 262px;
    left: 0;
    right: 0;
    margin: 0;
    font-style: normal;
    font-size: 22px;
    line-height: 44px;
  }
  .website {
    font-size: 25px;
  }
  .social-links {
    position: absolute;
    bottom: 70px;
    left: 0;
    right: 0;
    display: flex;
    justify-content: center;
    gap: 90px;
    margin: 0;
    padding: 0;
    list-style: none;
    font-size: 23px;
  }
  .social-links li {
    display: flex;
    align-items: center;
    gap: 8px;
  }
  .social-marker {
    width: 20px;
    height: 20px;
    background: var(--accent);
  }
</style>
</head>
<body>
  <main class="business-card">
    <h1 class="agency-name">Dorlin Insurance Agency, Inc.</h1>
    <svg class="divider-swoosh" viewBox="0 0 820 40" aria-hidden="true">
      <path d="M0 36 C 250 30, 550 14, 820 2 C 560 18, 280 34, 0 38 Z" fill="var(--accent)"/>
    </svg>
    <h2 class="agent-name">Marcus Helgren</h2>
    <address class="contact-details">
      <div class="street">4375 West Tamber Lane Corvale, Ohio</div>
      <div class="zip-phone">45192 555-281-7496</div>
      <div class="website">www.dorlinagency.example</div>
    </address>
    <ul class="social-links">
      <li><span class="social-marker"></span>Circlebook</li>
      <li><span class="social-marker"></span>ProLink</li>
      <li><span class="social-marker"></span>Gather+</li>
    </ul>
  </main>
</body>
</html>
```